依頼詳細
載内容詳細に関しては、別添のExcel資料を参照してください。

・ターゲット
BtoB
マンションの管理組合や管理業者
BtoC
防水工事系の仕事経験者の方で仕事を探している方

・カラーイメージ
青系
ロゴで使用されている青色を使用して、デザインお願いします。
▼参考
https://www.tamaori-rinku.jp/

・デザイン、ムード
参考のように企業らしい堅めのイメージでデザインお願いします
▼参考
http://www.nagisetec-lab.biz
https://www.morikuni-kei.co.jp/

配置やデザイン等はアレンジしていただいて構いません。
また、縦に制限はありません。

レスポンシブデザインのサイトで、bootstrap4を利用しコーディングする予定になります。

デザイン幅は2000px、コンテンツの幅はbootstrap4デフォルトのの1110pxを基準としてください。
ただし、最近のデザインの流行を取りいれて、フルワイドや、1200~1500px程度の幅のコンテンツをバランスよくレイアウトしてください。
コンテンツ配置は基本12分割になります。がデザインによっては、多少逸脱してもかまいません。
bootstrap4、12分割グリッドの基準のPSDも資料として添付しております。
ご参考になさってください。

本分のフォントはゴシック系は游ゴシック、メイリオ、明朝系は遊明朝でお願いします。
飾り文字はフリーフォントか、googleフォントを利用してください。

メイン画像部分・グローバルメニューは、ワイド適用でお願いします。

不明点、質問などありましたらメッセージ等でご連絡ください。
サイトURL
ページ数
1ページ
希望イメージ
シンプル 複雑
単色 カラフル
暗い 明るい
日常 高級
遊び心 厳粛
未来的 伝統的
女性的 男性的
希望する色
青系、水色系
納品ファイル
• 高解像度JPG (.jpg)
• フォトショップ形式 (.psd)
補足説明
・資料上はサイト名(社名)や住所などは伏字にしております。
ご提案時点ではそのまま作成をお願いします。

・使用画像は当選後こちらで用意します。
ご提案時点では前項同様に、カンプデータ等をご使用のうえ、当選後に本内容へ差し替え修正をお願いします。
また、雰囲気が合っていれば、指定外の画像を追加掲載いただいてOKです。

・当選前提となった方は正式な社名及び連絡先をお伝えしますので修正対応をお願いします。

お客様が希望されていたデザインイメージにピッタリだったため。

数多くの素晴らしい提案をいただきありがとうございました。
また次回もご参加よろしくお願いいたします。

```html
<!DOCTYPE html>
<html lang="ja">
<head>
<meta charset="utf-8">
<title>株式会社アオミネ | 防水工事・外壁補修</title>
<link href="https://fonts.googleapis.com/css2?family=Noto+Sans+JP:wght@400;500;700&family=Cormorant+Garamond:wght@500;600&display=swap" rel="stylesheet">
<style>
:root{
  --blue:#1a7fd0;
  --blue-dark:#0d4f8c;
  --navy:#17345c;
  --sky:#e6f2fb;
  --ghost:#c9d6e6;
  --text:#333a44;
  --muted:#7a8696;
  --white:#fff;
}
*{margin:0;padding:0;box-sizing:border-box}
html,body{width:704px;height:1200px;overflow:hidden;background:var(--white)}
body{font-family:"Noto Sans JP",sans-serif;color:var(--text);position:relative}
.abs{position:absolute}
/* header */
.site-header{left:0;top:0;width:704px;height:46px;background:var(--white);display:flex;align-items:center;padding-left:18px;z-index:3}
.brand{display:flex;align-items:center;gap:6px;font-weight:700;font-size:11px;color:var(--blue-dark);letter-spacing:.08em}
.brand-dot{width:12px;height:12px;border-radius:50%;background:var(--blue)}
.global-nav{display:flex;margin-left:120px}
.global-nav a{font-size:7px;color:var(--text);text-decoration:none;padding:0 10px;line-height:46px;text-align:center;position:relative}
.global-nav a.current{color:var(--blue)}
.global-nav a.current::after{content:"";position:absolute;left:8px;right:8px;bottom:10px;height:2px;background:var(--blue)}
.header-tel{margin-left:auto;background:var(--blue);color:var(--white);height:46px;width:112px;display:flex;flex-direction:column;justify-content:center;align-items:center}
.header-tel small{font-size:5.5px}
.header-tel strong{font-size:11px;letter-spacing:.04em}
/* hero */
.hero{left:0;top:46px;width:704px;height:236px;background:var(--white)}
.hero-photo{left:246px;top:0;width:458px;height:236px;background:linear-gradient(180deg,#cfe3f3 0%,#e8eef2 45%,#b9c8b0 80%,#8fa987 100%)}
.hero-copy{left:90px;top:40px;color:var(--blue);font-size:18px;font-weight:500;line-height:1.5;letter-spacing:.04em}
.hero-copy span{background:rgba(255,255,255,.85);padding:0 2px}
.hero-ghost{left:300px;top:20px;font-family:"Cormorant Garamond",serif;font-size:13px;color:rgba(255,255,255,.8);letter-spacing:.2em}
/* sections */
.ghost-word{font-family:"Cormorant Garamond",serif;font-weight:600;color:var(--ghost);font-size:54px;line-height:1;opacity:.7;letter-spacing:.02em}
.sec-title{font-size:13px;font-weight:700;color:var(--navy);letter-spacing:.1em}
.sec-title::first-letter{color:var(--blue)}
.about-skyline{left:0;top:378px;width:704px;height:92px;background:linear-gradient(180deg,rgba(230,242,251,0) 0%,#dbe9f6 60%,#eef5fb 100%)}
.about-text{left:200px;top:350px;width:304px;text-align:center;font-size:6.5px;line-height:1.9;color:var(--muted)}
.cards{left:153px;top:532px;display:flex;gap:14px}
.card{width:121px;height:82px;background:linear-gradient(160deg,#6f8aa3,#34485e);display:flex;align-items:center;justify-content:center}
.card span{color:var(--white);font-size:10px;font-weight:700;letter-spacing:.1em;border:1px solid rgba(255,255,255,.8);padding:4px 8px}
.case-grid{left:153px;top:692px;display:grid;grid-template-columns:repeat(4,94px);grid-auto-rows:44px;gap:6px}
.case-intro{background:var(--navy);color:var(--white);font-size:5.5px;line-height:1.7;padding:7px}
.case-photo{background:linear-gradient(150deg,#e5eef6,#9fb3c6)}
.btn{display:block;background:var(--blue);color:var(--white);font-size:6px;text-align:center;line-height:16px;width:60px;border-radius:1px;letter-spacing:.08em}
.recruit-banner{left:153px;top:930px;width:392px;height:115px;background:linear-gradient(120deg,#8ec3ea,#3c8fd0 60%,#2a73b5)}
.recruit-banner h3{position:absolute;left:0;right:0;top:32px;text-align:center;color:var(--white);font-size:14px;letter-spacing:.15em}
.recruit-banner .btn{position:absolute;left:166px;top:68px;background:var(--white);color:var(--blue)}
.site-footer{left:0;top:1082px;width:704px;height:104px;background:linear-gradient(180deg,#e9eef3,#d3dde6)}
.footer-brand{left:155px;top:14px}
.footer-info{left:155px;top:40px;font-size:5.5px;line-height:1.8;color:var(--text)}
.footer-nav{left:300px;top:80px;display:flex;gap:14px;font-size:5.5px;color:var(--text)}
.copyright{left:0;top:1186px;width:704px;height:14px;background:var(--navy);color:var(--white);font-size:5px;text-align:center;line-height:14px}
</style>
</head>
<body>
<header class="site-header abs">
  <div class="brand"><span class="brand-dot"></span>AOMINE</div>
  <nav class="global-nav">
    <a class="current">ホーム</a><a>業務内容</a><a>施工実績</a><a>会社概要</a><a>採用情報</a><a>お問い合わせ</a>
  </nav>
  <div class="header-tel"><small>お気軽にお問い合わせください</small><strong>03-4512-7788</strong></div>
</header>

<section class="hero abs">
  <div class="hero-photo abs" role="img" aria-label="マンションを背景に歩く家族の写真"></div>
  <p class="hero-ghost abs">SAFETY &amp; SECURITY</p>
  <h1 class="hero-copy abs"><span>安心安全の生活を</span><br><span>当たり前にするためのお手伝い</span></h1>
</section>

<div class="about-skyline abs" role="img" aria-label="淡い青の街並みの写真"></div>
<p class="ghost-word abs" style="left:330px;top:296px">About Us</p>
<h2 class="sec-title abs" style="left:300px;top:326px">私たちについて</h2>
<p class="about-text abs">私たちは、防水工事を中心に<br>建物の寿命を延ばし、住まう方の暮らしを守るお手伝いをしています。<br>確かな技術と誠実な対応で、管理組合・管理会社の皆様に信頼される<br>パートナーを目指し、一つひとつの現場に丁寧に向き合っています。</p>

<p class="ghost-word abs" style="left:153px;top:478px">Business</p>
<h2 class="sec-title abs" style="left:300px;top:506px">業務内容</h2>
<div class="cards abs">
  <div class="card" role="img" aria-label="防水工事の施工写真"><span>防水工事</span></div>
  <div class="card" role="img" aria-label="外壁補修工事の施工写真"><span>外壁補修工事</span></div>
  <div class="card" role="img" aria-label="外壁塗装の施工写真"><span>外壁塗装</span></div>
</div>

<p class="ghost-word abs" style="left:300px;top:636px">Case</p>
<h2 class="sec-title abs" style="left:300px;top:664px">施工実績</h2>
<div class="case-grid abs">
  <div class="case-intro">これまでに手がけた施工事例の一部をご紹介します。マンションの屋上防水から外壁まで幅広く対応しています。</div>
  <div class="case-photo" role="img" aria-label="施工現場の写真"></div>
  <div class="case-photo" role="img" aria-label="施工現場の写真"></div>
  <div class="case-photo" role="img" aria-label="施工現場の写真"></div>
  <div class="case-photo" role="img" aria-label="施工現場の写真"></div>
  <div class="case-photo" role="img" aria-label="施工現場の写真"></div>
  <div class="case-photo" role="img" aria-label="施工現場の写真"></div>
  <div class="case-photo" role="img" aria-label="施工現場の写真"></div>
  <div class="case-photo" role="img" aria-label="施工現場の写真"></div>
  <div class="case-photo" role="img" aria-label="施工現場の写真"></div>
  <div class="case-photo" role="img" aria-label="施工現場の写真"></div>
  <div class="case-photo" role="img" aria-label="施工現場の写真"></div>
</div>
<a class="btn abs" style="left:322px;top:846px">View more</a>

<p class="ghost-word abs" style="left:153px;top:890px">Recruit</p>
<div class="recruit-banner abs" role="img" aria-label="青く色付けされた働く人々の写真">
  <h3>採用情報</h3>
  <a class="btn">View more</a>
</div>

<footer class="site-footer abs" role="img" aria-label="淡い色調の建物写真の背景">
  <div class="brand footer-brand abs"><span class="brand-dot"></span>AOMINE</div>
  <p class="footer-info abs">株式会社アオミネ<br>〒100-0000 東京都千代田区青嶺町1-2-3<br>TEL 03-4512-7788</p>
  <nav class="footer-nav abs"><span>ホーム</span><span>業務内容</span><span>施工実績</span><span>会社概要</span><span>採用情報</span><span>お問い合わせ</span></nav>
</footer>
<p class="copyright abs">© AOMINE Co., Ltd. All Rights Reserved.</p>
</body>
</html>
```